Marn-ridge Tide Harbor Custom Brokers Limited

Name: Dorvella Hastings
Title: Customs Broker
Address: Shop 9 Birchfield Commercial Complex
207-209 Harlow Road
Kingston 8
Telephone: (876)
Email: tideharborport@quillmail.example

```html
<!DOCTYPE html>
<html lang="en">
<head>
<meta charset="utf-8">
<title>Marn-ridge Tide Harbor Custom Brokers Limited – Business Card</title>
<link rel="stylesheet" href="https://fonts.googleapis.com/css2?family=Lato:wght@300;400;700;900&display=swap">
<style>
  :root {
    --navy: #1b2a4e;
    --gold: #e3a21a;
    --grey: #8a8f99;
    --paper: #fbfbfa;
    --backdrop: #e9e6e1;
  }
  * { margin: 0; padding: 0; box-sizing: border-box; }
  html, body { width: 1200px; height: 800px; overflow: hidden; }
  body {
    background: var(--backdrop);
    font-family: "Lato", sans-serif;
    color: var(--navy);
    display: flex;
    align-items: center;
    justify-content: center;
    gap: 40px;
  }
  .card {
    position: relative;
    width: 540px;
    height: 309px;
    background: var(--paper);
    box-shadow: 0 6px 18px rgba(0,0,0,0.12);
  }
  .brand {
    display: flex;
    align-items: center;
    gap: 10px;
  }
  .brand-dot {
    width: 16px; height: 16px;
    border-radius: 50%;
    background: var(--gold);
    flex-shrink: 0;
  }
  .brand-name {
    font-weight: 900;
    color: var(--navy);
    text-transform: uppercase;
    line-height: 1.15;
    letter-spacing: 0.04em;
  }
  /* Front */
  .card-front .brand {
    position: absolute;
    top: 44px;
    right: 40px;
  }
  .card-front .brand-name { font-size: 15px; }
  .holder {
    position: absolute;
    left: 34px;
    right: 26px;
    top: 128px;
  }
  .holder-row {
    display: flex;
    align-items: flex-end;
  }
  .holder-name {
    font-size: 27px;
    font-weight: 900;
    letter-spacing: 0.02em;
    text-transform: uppercase;
    line-height: 1.1;
    white-space: nowrap;
  }
  .rule {
    flex: 1;
    height: 2px;
    background: var(--gold);
    margin: 0 0 4px 14px;
  }
  .holder-title {
    font-size: 15px;
    font-weight: 300;
    text-transform: uppercase;
    letter-spacing: 0.04em;
    margin-top: 3px;
  }
  .contact {
    position: absolute;
    left: 56px;
    top: 200px;
    font-size: 14px;
    line-height: 1.35;
  }
  .contact .address {
    font-weight: 900;
    text-transform: uppercase;
    font-size: 14.5px;
    margin-top: 2px;
  }
  /* Back */
  .card-back {
    display: flex;
    align-items: center;
    justify-content: center;
  }
  .card-back .brand-name { font-size: 21px; }
  .card-back .brand-dot { width: 24px; height: 24px; }
</style>
</head>
<body>
  <section class="card card-front">
    <div class="brand">
      <span class="brand-dot"></span>
      <span class="brand-name">Marn-ridge Tide Harbor<br>Custom Brokers Limited</span>
    </div>
    <div class="holder">
      <div class="holder-row">
        <h1 class="holder-name">Dorvella Hastings</h1>
        <span class="rule"></span>
      </div>
      <p class="holder-title">Customs Broker</p>
    </div>
    <div class="contact">
      <p>Tel. (876)555 0142</p>
      <p>E-mail. tideharborport@quillmail.example</p>
      <p class="address">Shop 9 Birchfield Commercial Complex<br>207-209 Harlow Road, Kingston 8</p>
    </div>
  </section>

  <section class="card card-back">
    <div class="brand">
      <span class="brand-dot"></span>
      <span class="brand-name">Marn-ridge Tide Harbor<br>Custom Brokers Limited</span>
    </div>
  </section>
</body>
</html>
```